Market Research firm needs updated business cards with new logo

We need the logo to be included somewhere on the card (attached). We would also like the phrases "Independent, Objective, Comprehensive" and "Research You Can Trust" somewhere on the card. Front or back. Our colors are hex codes 6075a7, e48d25 and 5a5b5b. Though you are certainly not limited to those shades, whatever you produce should coordinate with them. I have also attached our favicon. Feel free to use it in your design, but please do not use it to replace the full logo.

Contact Information for Business Card

see project description

Font styles to use
Other font styles liked:
• Open Sans

Requirements
Must have
• the logo
• We use Open Sans font

```html
<!DOCTYPE html>
<html lang="en">
<head>
<meta charset="utf-8">
<title>Veridan Research – Business Card</title>
<link rel="stylesheet" href="https://fonts.googleapis.com/css2?family=Open+Sans:wght@400;600;700&display=swap">
<style>
  :root {
    --stage: #000000;
    --paper: #ffffff;
    --slate: #66737f;
    --slate-text: #5f6873;
    --orange: #f07f22;
    --charcoal: #555659;
    --outline: #4a4f55;
  }
  * { margin: 0; padding: 0; box-sizing: border-box; }
  html, body { width: 1200px; height: 1000px; overflow: hidden; background: var(--stage); }
  body { position: relative; font-family: "Open Sans", Arial, sans-serif; }

  .card { position: absolute; left: 307px; width: 589px; height: 337px; background: var(--paper); overflow: hidden; }
  .card--front { top: 156px; height: 336px; }
  .card--back { top: 508px; }

  .brand { position: absolute; display: flex; align-items: center; color: var(--slate-text); font-weight: 400; white-space: nowrap; }
  .brand__dot { border-radius: 50%; background: var(--orange); flex: none; }
  .card--front .brand { left: 0; right: 0; top: 136px; justify-content: center; font-size: 46px; letter-spacing: -0.5px; }
  .card--front .brand__dot { width: 30px; height: 30px; margin-right: 14px; }
  .front__rule { position: absolute; left: 99px; width: 406px; top: 212px; height: 2px; background: var(--slate-text); }
  .front__tagline { position: absolute; left: 0; right: 0; top: 223px; text-align: center; font-size: 13px; font-weight: 700; color: var(--slate-text); letter-spacing: 0.3px; }
  .front__web { position: absolute; left: 0; right: 0; top: 292px; text-align: center; font-size: 17px; font-weight: 700; color: var(--slate-text); }

  .back__art { position: absolute; inset: 0; }
  .card--back .brand { left: 28px; top: 30px; font-size: 38px; letter-spacing: -0.5px; }
  .card--back .brand__dot { width: 24px; height: 24px; margin-right: 10px; }

  .badge__text { font-family: "Open Sans", Arial, sans-serif; font-size: 17px; font-weight: 600; fill: var(--paper); }

  .contact { position: absolute; left: 24px; top: 142px; color: var(--paper); }
  .contact__name { font-size: 20px; font-weight: 700; letter-spacing: 1.2px; line-height: 28px; }
  .contact__role { display: flex; align-items: center; gap: 6px; font-size: 14px; letter-spacing: 3px; line-height: 16px; }
  .contact__role::before { content: ""; display: block; width: 116px; height: 2px; background: var(--orange); margin-top: 2px; }
  .contact__list { list-style: none; margin-top: 14px; font-size: 16px; line-height: 24px; }
  .contact__list li { display: flex; align-items: center; gap: 5px; }
  .contact__list svg { width: 16px; height: 16px; flex: none; }
  .contact__rule { width: 281px; height: 2px; background: var(--orange); margin-top: 9px; }
  .contact__address { font-size: 16px; line-height: 24px; margin-top: 6px; }
</style>
</head>
<body>

<section class="card card--front">
  <div class="brand"><span class="brand__dot"></span>Veridan Research</div>
  <div class="front__rule"></div>
  <p class="front__tagline">INDEPENDENT • OBJECTIVE • COMPREHENSIVE</p>
  <p class="front__web">www.veridanresearch.com</p>
</section>

<section class="card card--back">
  <svg class="back__art" viewBox="0 0 589 337" width="589" height="337">
    <path d="M0,122 H300 C350,122 390,140 420,170 L470,170 C495,120 492,55 458,0 H589 V337 H0 Z" fill="var(--slate)"/>
    <path d="M0,117 H302 C355,117 395,135 430,170" fill="none" stroke="var(--orange)" stroke-width="20"/>
    <path d="M0,106 H302 C360,106 400,125 440,160" fill="none" stroke="var(--outline)" stroke-width="1.5"/>
    <path d="M455,0 C495,55 508,115 505,185" fill="none" stroke="var(--orange)" stroke-width="16"/>
    <path d="M446,0 C487,55 499,115 497,185" fill="none" stroke="var(--outline)" stroke-width="1.2"/>
    <rect x="0" y="325" width="295" height="12" fill="var(--orange)"/>
    <rect x="295" y="325" width="294" height="12" fill="var(--charcoal)"/>
    <circle cx="431" cy="224" r="96" fill="var(--orange)" stroke="var(--outline)" stroke-width="1.2"/>
    <defs>
      <path id="badge-arc" d="M381.5,174.5 A70,70 0 1,1 396,284.6"/>
    </defs>
    <text class="badge__text" letter-spacing="2">
      <textPath href="#badge-arc" textLength="300" lengthAdjust="spacing">RESEARCH YOU CAN TRUST</textPath>
    </text>
  </svg>

  <div class="brand"><span class="brand__dot"></span>Veridan Research</div>

  <div class="contact">
    <p class="contact__name">YOUR NAMEXXX</p>
    <p class="contact__role">Owner</p>
    <ul class="contact__list">
      <li><svg viewBox="0 0 16 16"><circle cx="8" cy="8" r="7" fill="none" stroke="#f07f22" stroke-width="1.5"/><path d="M5.5,4.5 l1.5,0 l0.6,2 l-1,0.8 c0.6,1.3 1.3,2 2.6,2.6 l0.8,-1 l2,0.6 l0,1.5 c-3.5,0.5 -7,-3 -6.5,-6.5z" fill="#f07f22"/></svg>Office : (999) 555-3555</li>
      <li><svg viewBox="0 0 16 16"><rect x="4" y="1" width="8" height="14" rx="1.5" fill="none" stroke="#f07f22" stroke-width="1.5"/><circle cx="8" cy="12.5" r="0.9" fill="#f07f22"/></svg>Cell &nbsp;&nbsp;: (999) 555-3555</li>
      <li><svg viewBox="0 0 16 16"><path d="M1,6 L8,1.5 L15,6 V14 H1 Z" fill="#f07f22"/><path d="M1,6 L8,10.5 L15,6" fill="none" stroke="#66737f" stroke-width="1.2"/></svg>hello@veridanresearch.com</li>
    </ul>
    <div class="contact__rule"></div>
    <p class="contact__address">PO Box 0000, Sjnn Low, AZ dfdfd</p>
  </div>
</section>

</body>
</html>
```